Business Card Design

An energy company designed around renewable energy and energy storage that focuses on providing its energy at points on the grid that reduce costs and add value to the system.

Industry/Entity Type

Business

Contact Information for Business Card

Martin Dellacroix
Executive Vice President
41 K ST NE
Washington, DC 20017
240-555-0187
mdellacroix@brightvaleenergy.example

```html
<!DOCTYPE html>
<html lang="en">
<head>
<meta charset="utf-8">
<title>Brightvale Energy — Business Card</title>
<link rel="stylesheet" href="https://fonts.googleapis.com/css2?family=Cabin:wght@400;500;600;700&display=swap">
<style>
  :root {
    --page: #e9e6e1;
    --card: #2e2e2c;
    --ink: #ffffff;
    --green: #5cb935;
  }
  * { margin: 0; padding: 0; box-sizing: border-box; }
  html, body {
    width: 1200px;
    height: 1200px;
    overflow: hidden;
    background: var(--page);
    font-family: "Cabin", "Gill Sans", sans-serif;
  }
  .business-card {
    position: absolute;
    left: 100px;
    top: 314px;
    width: 1000px;
    height: 572px;
    background: var(--card);
    color: var(--ink);
    box-shadow: 0 6px 18px rgba(0,0,0,0.18);
  }
  .wordmark {
    position: absolute;
    left: 120px;
    top: 96px;
    font-size: 64px;
    font-weight: 500;
    line-height: 0.98;
    color: var(--ink);
    letter-spacing: 0.5px;
  }
  .divider {
    position: absolute;
    left: 0;
    top: 280px;
    width: 560px;
    height: 3px;
    background: var(--green);
  }
  .identity {
    position: absolute;
    right: 52px;
    top: 262px;
    text-align: right;
  }
  .identity .person-name {
    font-size: 30px;
    font-weight: 600;
    color: var(--green);
    letter-spacing: 0.5px;
  }
  .identity .person-title {
    font-size: 26px;
    font-weight: 700;
    color: var(--ink);
    margin-top: 2px;
  }
  .contact-list {
    position: absolute;
    left: 62px;
    top: 368px;
    list-style: none;
  }
  .contact-list li {
    display: flex;
    align-items: center;
    gap: 18px;
    font-size: 24px;
    line-height: 36px;
    letter-spacing: 0.4px;
  }
  .contact-list svg { width: 26px; height: 26px; flex: none; }
  .address {
    position: absolute;
    right: 52px;
    top: 430px;
    text-align: right;
    font-size: 24px;
    line-height: 34px;
    font-style: normal;
    letter-spacing: 0.4px;
  }
</style>
</head>
<body>
  <section class="business-card">
    <div class="wordmark">Brightvale<br>Energy</div>
    <div class="divider"></div>

    <div class="identity">
      <div class="person-name">Martin Dellacroix</div>
      <div class="person-title">Executive Vice President</div>
    </div>

    <ul class="contact-list">
      <li>
        <svg viewBox="0 0 26 26" aria-hidden="true">
          <circle cx="13" cy="13" r="12" fill="none" stroke="var(--green)" stroke-width="2"/>
          <path d="M9 7.5l2.5 0 1 3-1.6 1.2a7 7 0 0 0 3.4 3.4l1.2-1.6 3 1v2.5a1.5 1.5 0 0 1-1.6 1.5A10 10 0 0 1 7.5 9.1 1.5 1.5 0 0 1 9 7.5z" fill="var(--green)"/>
        </svg>
        <span class="phone">240-555-0187</span>
      </li>
      <li>
        <svg viewBox="0 0 26 26" aria-hidden="true">
          <circle cx="13" cy="13" r="12" fill="var(--green)"/>
          <rect x="6.5" y="8.5" width="13" height="9" fill="none" stroke="var(--card)" stroke-width="1.6"/>
          <path d="M6.5 8.5l6.5 5.5 6.5-5.5" fill="none" stroke="var(--card)" stroke-width="1.6"/>
        </svg>
        <span class="email">mdellacroix@brightvaleenergy.example</span>
      </li>
    </ul>

    <address class="address">
      41 K ST NE<br>
      Washington, DC 20017
    </address>
  </section>
</body>
</html>
```